Flyer Design for Promoting Arborist Business

Hi guys,
***UPDATE: File pack is available here: https://www.filecrate-example.net/sh/x7k2qq/BBbR4tLmZ9wPdVs?dl=0
We've are a high-end arborist business in Edinburgh and we're now looking to create some promotional flyers to attract new business.
This is an open brief and we're looking for inspiration from our designer.
Our target market for the flyers is people who cannot readily access our online material (e.g. elderly people without internet access), so therefore has to be easily understood.
Trust is a central part of our business and we'd like our photographs on the flyer to build that trust.
The primary method of contact will be telephone, therefore we'd like our phone numbers to be front and centre.
You can see our website here: www.fernhollowtreecare.com
We have a full pack of design material for our logo which can be shared. This includes colours, fonts and logo. It's all as per our website.
Inspire us!
Best,
Malcolm

Look and feel
Each slider illustrates characteristics of the customer's brand and the style your logo design should communicate.

```html
<!DOCTYPE html>
<html lang="en">
<head>
<meta charset="utf-8">
<title>Fern Hollow Tree Care – Flyer</title>
<link href="https://fonts.googleapis.com/css2?family=Arimo:wght@400;700&display=swap" rel="stylesheet">
<style>
  :root {
    --brand-red: #b0161b;
    --ink: #2b2b2b;
    --backdrop: #b3b3b3;
    --paper: #ffffff;
    --bar: #1c1c1c;
    --soft-grey: #d6d6d9;
  }
  * { box-sizing: border-box; margin: 0; padding: 0; }
  html, body { width: 1200px; height: 1200px; overflow: hidden; background: var(--backdrop); }
  body { position: relative; font-family: "Arimo", Arial, sans-serif; color: var(--ink); }

  .flyer {
    position: absolute; left: 218px; top: 62px; width: 761px; height: 1076px;
    background: linear-gradient(100deg, var(--paper) 52%, var(--soft-grey) 100%);
    overflow: hidden;
  }

  .header { position: absolute; left: 0; top: 0; width: 100%; height: 174px; background: var(--paper); border-bottom: 4px solid var(--brand-red); }
  .brand { position: absolute; left: 208px; top: 86px; transform: translate(-50%, -50%); display: flex; align-items: center; gap: 10px; white-space: nowrap; }
  .brand-dot { width: 18px; height: 18px; border-radius: 50%; background: var(--brand-red); }
  .brand-name { font-size: 27px; font-weight: 700; color: var(--ink); }
  .header-divider { position: absolute; left: 422px; top: 31px; width: 3px; height: 114px; background: var(--ink); }
  .tagline { position: absolute; right: 43px; top: 40px; text-align: right; font-weight: 700; font-size: 26px; line-height: 31px; }
  .tagline .red { color: var(--brand-red); }

  .hero { position: absolute; left: 0; top: 174px; width: 761px; height: 500px; }

  .photo-ring { position: absolute; border: 6px solid var(--brand-red); border-radius: 50%; box-shadow: 0 0 0 3px #fff; }
  .photo-ring.team { left: 292px; top: 474px; width: 216px; height: 216px; background: linear-gradient(160deg, #c9b79a, #6f7a3f 60%, #5a3a2a); }
  .photo-ring.climber { left: 529px; top: 434px; width: 220px; height: 220px; background: linear-gradient(140deg, #d8d8c8, #b03a2e 45%, #7a8a4a); }

  .services { position: absolute; left: 43px; top: 662px; list-style: none; }
  .service { display: flex; align-items: center; height: 55px; }
  .service-icon { width: 46px; height: 46px; margin-right: 12px; flex: none; }
  .service-name { font-size: 21px; font-weight: 700; color: var(--ink); white-space: nowrap; }

  .about { position: absolute; right: 43px; top: 694px; width: 328px; text-align: right; }
  .about h2 { font-size: 20px; font-weight: 700; line-height: 22px; white-space: nowrap; }
  .about .sub { font-size: 14.5px; line-height: 18px; color: var(--brand-red); margin-bottom: 18px; }
  .about p { font-size: 14.5px; line-height: 18.4px; margin-bottom: 18.4px; }

  .call-bar {
    position: absolute; left: 0; bottom: 0; width: 100%; height: 56px; background: var(--bar);
    display: flex; align-items: center; justify-content: flex-end; gap: 22px; padding-right: 43px;
    color: #fff; font-weight: 700; font-size: 26px; white-space: nowrap;
  }
  .call-bar .number { display: flex; align-items: center; gap: 6px; }
  .call-bar svg { fill: var(--brand-red); }
</style>
</head>
<body>
<div class="flyer">
  <header class="header">
    <div class="brand"><span class="brand-dot"></span><span class="brand-name">Fern Hollow Tree Care</span></div>
    <div class="header-divider"></div>
    <div class="tagline">
      <div class="red">Professional</div>
      <div>Edinburgh-Based</div>
      <div class="red">Tree Surgeons</div>
    </div>
  </header>

  <svg class="hero" viewBox="0 0 761 500">
    <defs>
      <linearGradient id="heroFill" x1="0" y1="0" x2="1" y2="1">
        <stop offset="0" stop-color="#6b5a4c"/>
        <stop offset="0.45" stop-color="#4a3b33"/>
        <stop offset="1" stop-color="#8a6a52"/>
      </linearGradient>
      <linearGradient id="swoosh" x1="0" y1="0" x2="1" y2="0">
        <stop offset="0" stop-color="#262626"/>
        <stop offset="0.55" stop-color="#3a3a3a"/>
        <stop offset="1" stop-color="#9a9a9c" stop-opacity="0.6"/>
      </linearGradient>
    </defs>
    <path class="hero-swoosh" d="M0 420 C150 465 310 470 420 440 C520 400 640 375 761 355 V395 C640 410 530 440 430 470 C310 500 150 478 0 445 Z" fill="url(#swoosh)"/>
    <path class="hero-photo" d="M0 0 H761 V355 C640 375 520 400 420 440 C310 470 150 465 0 420 Z" fill="url(#heroFill)" role="img" aria-label="Photo of a climbing arborist cutting a large tree limb above a house roof"/>
  </svg>

  <div class="photo-ring team" role="img" aria-label="Photo of two arborists in safety gear standing beneath a tree"></div>
  <div class="photo-ring climber" role="img" aria-label="Photo of an arborist in red gear trimming a branch"></div>

  <ul class="services">
    <li class="service">
      <svg class="service-icon" viewBox="0 0 46 46"><circle cx="23" cy="23" r="21" fill="none" stroke="var(--brand-red)" stroke-width="1.6"/><path d="M9 24 H37 M18 24 L13 18 M24 24 L29 17 M30 24 L34 29" stroke="var(--brand-red)" stroke-width="1.6" fill="none"/></svg>
      <span class="service-name">Aerial Pruning</span>
    </li>
    <li class="service">
      <svg class="service-icon" viewBox="0 0 46 46"><circle cx="23" cy="23" r="21" fill="none" stroke="var(--brand-red)" stroke-width="1.6"/><ellipse cx="23" cy="16" rx="10" ry="4" fill="none" stroke="var(--brand-red)" stroke-width="1.6"/><path d="M13 16 V31 H33 V16" fill="var(--brand-red)"/></svg>
      <span class="service-name">Stump Removal</span>
    </li>
    <li class="service">
      <svg class="service-icon" viewBox="0 0 46 46"><circle cx="23" cy="23" r="21" fill="none" stroke="var(--brand-red)" stroke-width="1.6"/><path d="M25 8 L16 25 H22 L19 38 L30 19 H24 Z" fill="var(--brand-red)"/></svg>
      <span class="service-name">Storm Damage</span>
    </li>
    <li class="service">
      <svg class="service-icon" viewBox="0 0 46 46"><circle cx="23" cy="23" r="21" fill="none" stroke="var(--brand-red)" stroke-width="1.6"/><rect x="15" y="12" width="16" height="22" fill="none" stroke="var(--brand-red)" stroke-width="1.6"/><path d="M18 18 H28 M18 22 H28 M18 26 H28 M18 30 H25" stroke="var(--brand-red)" stroke-width="1.4"/></svg>
      <span class="service-name">Tree Surveys</span>
    </li>
    <li class="service">
      <svg class="service-icon" viewBox="0 0 46 46"><circle cx="23" cy="23" r="21" fill="none" stroke="var(--brand-red)" stroke-width="1.6"/><path d="M13 34 L27 18 M24 12 L33 21 L29 24 L22 16 Z" stroke="var(--brand-red)" stroke-width="1.8" fill="none"/></svg>
      <span class="service-name">Felling and Dismantling</span>
    </li>
    <li class="service">
      <svg class="service-icon" viewBox="0 0 46 46"><circle cx="23" cy="23" r="21" fill="none" stroke="var(--brand-red)" stroke-width="1.6"/><path d="M23 36 V20 M23 24 L15 16 M23 22 L31 14 M23 28 L30 22 M23 28 L16 23" stroke="var(--brand-red)" stroke-width="1.8" fill="none"/></svg>
      <span class="service-name">Crown Lifts and Reductions</span>
    </li>
  </ul>

  <section class="about">
    <h2>Fern Hollow Tree Care</h2>
    <div class="sub">Our Qualifications</div>
    <p>Our arborist team is trained in the latest arborist techniques and furnished with state-of-the-art equipment to ensure that your tree work is carried out to the highest standard, quickly and with maximum safety.</p>
    <p>We take great pride in our professionalism and the standard of our work and we're fully insured to carry out all our work for your peace of mind.</p>
    <p>We offer our emergency call-out service to make trees safe after acute damage, for example due to wind or limb release.</p>
  </section>

  <footer class="call-bar">
    <span>Call us now:</span>
    <span class="number"><svg width="28" height="22" viewBox="0 0 28 22"><path d="M2 8 C6 2 22 2 26 8 L22 11 L19 8 H9 L6 11 Z M7 12 H21 L24 20 H4 Z"/></svg>0131 496 0728</span>
    <span class="number"><svg width="16" height="24" viewBox="0 0 16 24"><path d="M3 1 H13 A2 2 0 0 1 15 3 V21 A2 2 0 0 1 13 23 H3 A2 2 0 0 1 1 21 V3 A2 2 0 0 1 3 1 Z M4 4 V18 H12 V4 Z"/></svg>07700 900 461</span>
  </footer>
</div>
</body>
</html>
```